Cosmetics Brand Logo and Bottle Label Design

We are creating a new cosmetics brand called "Nolan Whitby" and would like you to create an amazing logo and bottle label for this brand's new 100% pure argan oil product.
For the logo, we really like the logo's of Marin Calloway and Vessa. The text should be Sans Serif (without feet).
For the actual bottle label, please find attached labels of one of our competitors design which really like. We really like the simplicity and elegance of the design. The only difference is that our product will be using light turqoise as the brand color. Please feel free to add your own creativity into it as well.
Industry/Entity Type
Cosmetics
Logo Text
Nolan Whitby
Font styles to use

```html
<!DOCTYPE html>
<html lang="en">
<head>
<meta charset="utf-8">
<title>Nolan Whitby – Argan Oil Label</title>
<link rel="stylesheet" href="https://fonts.googleapis.com/css2?family=Josefin+Sans:wght@300;400&family=Open+Sans:wght@400&display=swap">
<style>
  :root {
    --backdrop: #ecedef;
    --label-turquoise: #67d5c6;
    --label-turquoise-shade: #5ccbbb;
    --stripe-light-green: #8fd43c;
    --stripe-deep-green: #3e9a2c;
    --ink: #263634;
  }
  html, body {
    margin: 0;
    padding: 0;
    width: 900px;
    height: 1200px;
    overflow: hidden;
    background: var(--backdrop);
  }
  .canvas {
    position: relative;
    width: 900px;
    height: 1200px;
  }
  .label {
    position: absolute;
    left: 130px;
    top: 100px;
    width: 640px;
    height: 1000px;
    background: linear-gradient(180deg, var(--label-turquoise) 0%, var(--label-turquoise-shade) 100%);
    color: var(--ink);
    text-align: center;
  }
  .stripe {
    position: absolute;
    left: 0;
    width: 100%;
  }
  .stripe--thin { height: 5px; background: var(--stripe-deep-green); }
  .stripe--wide { height: 11px; background: var(--stripe-light-green); }
  .stripe--top-thin { top: 34px; }
  .stripe--top-wide { top: 44px; }
  .stripe--bottom-wide { bottom: 44px; }
  .stripe--bottom-thin { bottom: 34px; }

  .brand-name {
    position: absolute;
    top: 410px;
    left: 0;
    width: 100%;
    margin: 0;
    font-family: "Josefin Sans", sans-serif;
    font-weight: 400;
    font-size: 62px;
    letter-spacing: 3px;
    text-transform: uppercase;
  }
  .product-tagline {
    position: absolute;
    top: 490px;
    left: 0;
    width: 100%;
    margin: 0;
    font-family: "Josefin Sans", sans-serif;
    font-weight: 300;
    font-size: 38px;
  }
  .product-type {
    position: absolute;
    top: 745px;
    left: 0;
    width: 100%;
    margin: 0;
    font-family: "Open Sans", sans-serif;
    font-size: 33px;
    line-height: 46px;
  }
  .volume {
    position: absolute;
    top: 885px;
    left: 0;
    width: 100%;
    margin: 0;
    font-family: "Open Sans", sans-serif;
    font-size: 28px;
    letter-spacing: 1px;
  }
</style>
</head>
<body>
  <main class="canvas">
    <section class="label" aria-label="Nolan Whitby argan oil bottle label">
      <div class="stripe stripe--thin stripe--top-thin"></div>
      <div class="stripe stripe--wide stripe--top-wide"></div>

      <h1 class="brand-name">Nolan Whitby</h1>
      <p class="product-tagline">100% pure argan oil</p>

      <p class="product-type">Organic<br>Moisturizing Oil</p>

      <p class="volume">50 mL 1.7 fl oz</p>

      <div class="stripe stripe--wide stripe--bottom-wide"></div>
      <div class="stripe stripe--thin stripe--bottom-thin"></div>
    </section>
  </main>
</body>
</html>
```